Modern and Elegant business card

A clean and modern but traditional business card is required to reflect the updated LOGO and the new website www.brivexalta.com

The old card as provided is a bit disjointed, crowded and not clear to read especially the company name which is almost hidden in the logo.

The card should take it's queues from the colours of the logo which are green, yellow and orange, bold but rich, not faded or washed out.

We are looking to drastically clean up and improve our old cards

Target Market(s)

Professional Consulting and Business/Government

Industry/Entity Type

Management Consulting

Contact Information for Business Card

The card needs to outlined the new Service Groups as seen on the new site: http://brivexalta.com/services/ New logo needs to be included
The usual info for phones, address and name and email

Font styles to use
Serif
Sans Serif

Colors
fbee3d
f78f20
9bcb3c

Requirements
Must have
• New logo as seen on the current site and provided here
• Service Groups as seen http://brivexalta.com/services/
• Needs to be functional and clean, well proportioned and organized
Nice to have
• Name of cities where offices are located

```html
<!DOCTYPE html>
<html lang="en">
<head>
<meta charset="utf-8">
<title>Brivexalta business card</title>
<link href="https://fonts.googleapis.com/css2?family=Roboto+Condensed:wght@400;500&display=swap" rel="stylesheet">
<style>
  :root {
    --backdrop: #b9bcbf;
    --front-top: #eef6dc;
    --front-bottom: #9bcb3c;
    --band-yellow: #d8db26;
    --ink: #14211a;
    --brand-green: #1f3b2b;
    --sun-orange: #f78f20;
    --sun-yellow: #fbee3d;
    --back-black: #0b0b0b;
    --contact-yellow: #f3d314;
    --white: #ffffff;
  }
  * { margin: 0; padding: 0; box-sizing: border-box; }
  html, body { width: 1200px; height: 1200px; overflow: hidden; }
  body {
    background: var(--backdrop);
    font-family: "Roboto Condensed", sans-serif;
    position: relative;
  }
  .card {
    position: absolute;
    left: 182px;
    width: 840px;
    height: 476px;
    overflow: hidden;
    box-shadow: 0 6px 18px rgba(0,0,0,.35);
  }
  /* Front */
  .card-front {
    top: 60px;
    background: linear-gradient(to bottom, var(--front-top) 0%, #c8e490 45%, var(--front-bottom) 100%);
  }
  .band-strip {
    position: absolute; left: 0; top: 54px; width: 72px; height: 125px;
    background: var(--band-yellow);
  }
  .band-main {
    position: absolute; left: 326px; top: 54px; right: 0; height: 125px;
    background: var(--band-yellow);
  }
  .brand-lockup {
    position: absolute; left: 72px; top: 54px; width: 254px; height: 125px;
    display: flex; align-items: center; justify-content: center; gap: 10px;
  }
  .brand-dot {
    width: 22px; height: 22px; border-radius: 50%; background: var(--sun-orange);
  }
  .brand-name {
    font-size: 36px; font-weight: 500; color: var(--brand-green); letter-spacing: 1px;
  }
  .tagline {
    position: absolute; left: 366px; top: 74px;
    font-size: 22px; line-height: 28px; color: var(--ink);
  }
  .front-web {
    position: absolute; left: 367px; top: 140px;
    font-size: 26px; color: var(--ink);
  }
  .services {
    position: absolute; left: 100px; top: 202px; list-style: none;
  }
  .services li {
    display: flex; align-items: center; gap: 12px;
    height: 36.6px; font-size: 22px; color: var(--ink);
  }
  .services svg { width: 20px; height: 20px; flex: none; }

  /* Back */
  .card-back {
    top: 664px;
    background: radial-gradient(ellipse at 50% 35%, #1d1d1d 0%, var(--back-black) 75%);
  }
  .back-brand {
    position: absolute; left: 0; right: 0; top: 160px;
    display: flex; align-items: center; justify-content: center; gap: 16px;
  }
  .back-brand .brand-dot { width: 34px; height: 34px; }
  .back-brand .brand-name {
    font-size: 72px; color: var(--white); letter-spacing: 3px; font-weight: 500;
  }
  .contact {
    position: absolute; display: flex; align-items: center; gap: 14px;
    font-size: 24px; color: var(--contact-yellow);
  }
  .contact .marker {
    width: 34px; height: 34px; border-radius: 50%; flex: none;
    background: #e9e9e9; border: 2px solid #bdbdbd;
  }
  .contact svg { width: 30px; height: 30px; flex: none; }
  .phone-ca { left: 92px; top: 330px; }
  .phone-us { left: 92px; top: 376px; }
  .email { left: 402px; top: 324px; }
  .web { left: 402px; top: 368px; }
</style>
</head>
<body>
  <section class="card card-front">
    <div class="band-strip"></div>
    <div class="band-main"></div>
    <div class="brand-lockup">
      <span class="brand-dot"></span>
      <span class="brand-name">Brivexalta</span>
    </div>
    <p class="tagline">Cross-border Canada- U.S. Business Strategy<br>consulting firm, established in 2010</p>
    <p class="front-web">www.brivexalta.com</p>
    <ul class="services">
      <li><svg viewBox="0 0 20 20"><path d="M2 11 L7 16 L18 3" fill="none" stroke="var(--ink)" stroke-width="3.5" stroke-linecap="round" stroke-linejoin="round"/></svg>Export Market Developent</li>
      <li><svg viewBox="0 0 20 20"><path d="M2 11 L7 16 L18 3" fill="none" stroke="var(--ink)" stroke-width="3.5" stroke-linecap="round" stroke-linejoin="round"/></svg>Business Startegy, Implementation and Project Management</li>
      <li><svg viewBox="0 0 20 20"><path d="M2 11 L7 16 L18 3" fill="none" stroke="var(--ink)" stroke-width="3.5" stroke-linecap="round" stroke-linejoin="round"/></svg>Energy Sector Strategy and Supply Chain Optimization</li>
      <li><svg viewBox="0 0 20 20"><path d="M2 11 L7 16 L18 3" fill="none" stroke="var(--ink)" stroke-width="3.5" stroke-linecap="round" stroke-linejoin="round"/></svg>Community and Economic Development</li>
      <li><svg viewBox="0 0 20 20"><path d="M2 11 L7 16 L18 3" fill="none" stroke="var(--ink)" stroke-width="3.5" stroke-linecap="round" stroke-linejoin="round"/></svg>Comercial /Rentail Business Optimization Strategy</li>
      <li><svg viewBox="0 0 20 20"><path d="M2 11 L7 16 L18 3" fill="none" stroke="var(--ink)" stroke-width="3.5" stroke-linecap="round" stroke-linejoin="round"/></svg>Strategic Communications, Branding and Social Media</li>
    </ul>
  </section>

  <section class="card card-back">
    <div class="back-brand">
      <span class="brand-dot"></span>
      <span class="brand-name">Brivexalta</span>
    </div>
    <div class="contact phone-ca"><span class="marker" role="img" aria-label="Canada office marker"></span>1 780 555 0142</div>
    <div class="contact phone-us"><span class="marker" role="img" aria-label="United States office marker"></span>1 772 555 0187</div>
    <div class="contact email">
      <svg viewBox="0 0 30 30"><text x="15" y="24" text-anchor="middle" font-size="28" font-family="Roboto Condensed, sans-serif" fill="var(--contact-yellow)">@</text></svg>
      info@brivexalta.com
    </div>
    <div class="contact web">
      <svg viewBox="0 0 30 30" fill="none" stroke="var(--contact-yellow)" stroke-width="1.6">
        <circle cx="15" cy="15" r="12"/>
        <ellipse cx="15" cy="15" rx="5.5" ry="12"/>
        <line x1="3" y1="15" x2="27" y2="15"/>
        <path d="M5 9 H25 M5 21 H25"/>
      </svg>
      www.brivexalta.com
    </div>
  </section>
</body>
</html>
```